"End of year wishes" - Electronic card

Velmora is a regulatory consulting company in the cosmetic sector. We provide premium services and have 12 years of experience.
Please visit our website for more information: https://velmora-example.com
Like every year, we would like to send an electronic design to our clients and partners to wish them happy holidays. This year, we would like to share two good news with them: offer them a surprise (to be revealed later on) and invite them to visit our new brand new website. We relay on your talent and imagination for the design! We need something very professional, serious, beautiful and in line with our graphic layout (see our company website)

Target Market(s)

cosmetic brands

Industry/Entity Type

Cosmetics

Requirements
Must have
• The following statement should be included to the design:

We wish you a Happy Holiday and a Marvelous New Year 2021!
As December is the month of giving, we have a surprise for you. Please contact your dedicated Account Manager to find out more!

Good news never comes alone, we've also updated our website in order to serve you better. We hope you like it as much as we do.
Please enjoy the experience: www.velmora-example.com

```html
<!DOCTYPE html>
<html lang="en">
<head>
<meta charset="utf-8">
<title>Velmora – Season's Greetings 2021</title>
<link rel="stylesheet" href="https://fonts.googleapis.com/css2?family=Signika:wght@500;600;700&display=swap">
<style>
  :root {
    --wine-deep: #5e0a12;
    --wine: #8e1420;
    --wine-bright: #b3222c;
    --gold-light: #ffe27a;
    --gold: #f5b92c;
    --gold-deep: #d88a12;
    --cream: #fbe9dc;
    --cream-shade: #e8b39a;
    --ribbon: #e0201c;
    --white: #ffffff;
  }
  html, body {
    margin: 0;
    padding: 0;
    width: 1200px;
    height: 900px;
    overflow: hidden;
    background: var(--wine-deep);
  }
  .card {
    position: relative;
    width: 1200px;
    height: 900px;
    overflow: hidden;
    background:
      radial-gradient(ellipse 60% 55% at 78% 45%, var(--wine-bright) 0%, transparent 70%),
      radial-gradient(ellipse 80% 70% at 30% 40%, var(--wine) 0%, var(--wine-deep) 100%);
    font-family: "Signika", sans-serif;
    color: var(--white);
  }
  .gold-text {
    background: linear-gradient(180deg, var(--gold-light) 0%, var(--gold) 55%, var(--gold-deep) 100%);
    -webkit-background-clip: text;
    background-clip: text;
    color: transparent;
  }
  .greeting {
    position: absolute;
    left: 30px;
    top: 10px;
    margin: 0;
    font-family: "Signika", sans-serif;
    font-weight: 700;
    line-height: 1;
    white-space: nowrap;
  }
  .greeting span { display: block; }
  .greeting .line-wish { font-size: 84px; letter-spacing: -0.5px; }
  .greeting .line-and { font-size: 46px; margin-top: 20px; }
  .greeting .line-year { font-size: 84px; margin-top: 4px; }

  .surprise-frame {
    position: absolute;
    left: -10px;
    top: 338px;
    width: 710px;
    height: 292px;
    border: 3px solid var(--gold);
    border-radius: 22px;
    background: linear-gradient(120deg, var(--wine-bright) 0%, var(--wine) 60%, #7a1019 100%);
    box-shadow: 0 0 24px rgba(255, 200, 90, 0.25);
  }
  .surprise-text {
    position: absolute;
    left: 32px;
    top: 388px;
    margin: 0;
    font-size: 29px;
    font-weight: 600;
    line-height: 44px;
    white-space: nowrap;
  }
  .bow-art {
    position: absolute;
    left: 525px;
    top: 455px;
    width: 190px;
    height: 170px;
    background: radial-gradient(ellipse 50% 50% at 50% 50%, var(--ribbon) 0%, rgba(224, 32, 28, 0.55) 45%, rgba(224, 32, 28, 0) 100%);
  }
  .website-note {
    position: absolute;
    left: 32px;
    top: 702px;
    margin: 0;
    font-size: 20.5px;
    font-weight: 500;
    line-height: 32px;
    white-space: nowrap;
  }
  .website-link {
    position: absolute;
    left: 32px;
    top: 808px;
    margin: 0;
    font-size: 31px;
    font-weight: 700;
    color: var(--gold);
    white-space: nowrap;
  }
  .tree-art {
    position: absolute;
    left: 780px;
    top: 150px;
    width: 400px;
    height: 690px;
    background:
      radial-gradient(ellipse 22% 10% at 50% 8%, rgba(255, 226, 122, 0.8) 0%, rgba(255, 226, 122, 0) 100%),
      radial-gradient(ellipse 46% 50% at 50% 55%, var(--cream) 0%, rgba(232, 179, 154, 0.75) 55%, rgba(232, 179, 154, 0) 100%);
  }
</style>
</head>
<body>
  <main class="card">
    <h1 class="greeting">
      <span class="line-wish gold-text">We wish you a Happy Holiday</span>
      <span class="line-and gold-text">and a Marvelous</span>
      <span class="line-year gold-text">New Year 2021!</span>
    </h1>

    <div class="surprise-frame"></div>
    <p class="surprise-text">
      As December is the month of giving,<br>
      we have a surprise for you.<br>
      Please contact your dedicated<br>
      Account Manager to find out more!
    </p>

    <div class="bow-art" role="img" aria-label="Red gift ribbon bow tied across the corner of the message box"></div>

    <p class="website-note">
      Good news never comes alone, we’ve also updated our website<br>
      in order to serve you better. We hope you like it as much as we do.
    </p>

    <p class="website-link">Please enjoy the experience: www.velmora-example.com</p>

    <div class="tree-art" role="img" aria-label="Illustrated cream Christmas tree with gold baubles, gold ribbon swirls and a shining gold star on top"></div>
  </main>
</body>
</html>
```